Simple elegant feminine design - Going out on my own as a Mortgage Broker.
My thoughts are the following details on the Front, middle of the card possibly? Phone and email smaller font than my name?
Marnie Veltrin
Finance Specialist
p: 0438 215 962
e: marnie@veltrinlending.com.au
Bottom of the card
residential / commercial / equipment
I would like the Font in Rose Gold maybe white or black background? or Possibly a stone grey - are you able to do a few options? I'd like them embossed
Then I had an idea as a simple logo as per the attached if you get the idea in my scribble, my initials, capital M attached to a small v that leads/follows into a circle? Thicker Font In Rose Gold, middle of the card at the back.
Very open to ideas though and what colour you think would look better with the Rose Gold.
Thanks so much for your help, I am not very creative and savvy with this stuff :-)
Industry/Entity Type
Finance
Contact Information for Business Card
Marnie Veltrin
p: 0438 215 962
Look and feel

```html
<!DOCTYPE html>
<html lang="en">
<head>
<meta charset="utf-8">
<title>Marnie's Business Cards</title>
<link rel="stylesheet" href="https://fonts.googleapis.com/css2?family=Fira+Sans:wght@300;400&display=swap">
<style>
  :root {
    --paper: #ffffff;
    --outline: #2a2a2a;
    --card-black: #060606;
    --rose: #f3b9b4;
    --rose-deep: #b8646e;
    --rose-mid: #d9878f;
    --rose-pale: #efd0cf;
    --rose-frame-a: #c57a83;
    --rose-frame-b: #e4a3a6;
  }
  * { margin: 0; padding: 0; box-sizing: border-box; }
  html, body {
    width: 1020px; height: 1200px; overflow: hidden;
    background: var(--paper);
  }
  .sheet {
    position: relative; width: 1020px; height: 1200px;
    border: 1px solid var(--outline);
    background: var(--paper);
    font-family: "Fira Sans", Arial, sans-serif;
    font-weight: 300;
    color: var(--rose);
  }
  .card-front {
    position: absolute; left: 66px; top: 51px; width: 883px; height: 539px;
    padding: 10px;
    background: linear-gradient(135deg, var(--rose-frame-a), var(--rose-frame-b) 40%, var(--rose-frame-a) 70%, var(--rose-frame-b));
  }
  .card-front__inner {
    position: relative; width: 100%; height: 100%;
    background: var(--card-black);
  }
  .front-text {
    position: absolute; left: 0; right: 0; text-align: center;
    white-space: nowrap; line-height: 1;
  }
  .holder-name { top: 102px; left: 36px; font-size: 51px; font-weight: 400; }
  .name-rule {
    position: absolute; left: 283px; top: 155px; width: 332px; height: 2px;
    background: var(--rose);
  }
  .holder-title { top: 163px; left: 36px; font-size: 35px; }
  .contact { font-size: 36px; display: flex; justify-content: center; align-items: center; gap: 10px; }
  .contact--phone { top: 273px; left: 36px; }
  .contact--email { top: 319px; left: 36px; }
  .contact svg { fill: var(--rose); }
  .services { top: 389px; left: 36px; font-size: 27px; word-spacing: 4px; }
  .card-back {
    position: absolute; left: 66px; top: 618px; width: 881px; height: 538px;
    background: var(--card-black); overflow: hidden;
  }
  .card-back__facets { position: absolute; left: 0; top: 0; }
  .card-back__name {
    position: absolute; left: 38px; top: 272px; width: 260px; text-align: center;
    font-size: 32px; font-weight: 400; color: var(--rose); white-space: nowrap;
  }
</style>
</head>
<body>
<div class="sheet">
  <section class="card-front">
    <div class="card-front__inner">
      <div class="front-text holder-name">Marnie Veltrin</div>
      <div class="name-rule"></div>
      <div class="front-text holder-title">Finance Specialist</div>
      <div class="front-text contact contact--phone">
        <svg width="26" height="26" viewBox="0 0 24 24" aria-hidden="true"><path d="M6.6 10.8a15.1 15.1 0 0 0 6.6 6.6l2.2-2.2c.3-.3.7-.4 1-.2 1.1.4 2.3.6 3.6.6.6 0 1 .4 1 1V20c0 .6-.4 1-1 1A17 17 0 0 1 3 4c0-.6.4-1 1-1h3.5c.6 0 1 .4 1 1 0 1.3.2 2.5.6 3.6.1.3 0 .7-.2 1z"/></svg>
        <span>0438 215 962</span>
      </div>
      <div class="front-text contact contact--email">
        <svg width="30" height="22" viewBox="0 0 30 22" aria-hidden="true"><path d="M1 1h28v20H1z M3 3v.6l12 9 12-9V3z M3 6.2V19h24V6.2l-12 9z" fill-rule="evenodd"/></svg>
        <span>marnie@veltrinlending.com.au</span>
      </div>
      <div class="front-text services">residential / &nbsp;commercial / &nbsp;equipment</div>
    </div>
  </section>

  <section class="card-back">
    <svg class="card-back__facets" width="881" height="538" viewBox="0 0 881 538" role="img" aria-label="Faceted rose gold geometric crystal artwork">
      <defs>
        <linearGradient id="facetTone" x1="0" y1="1" x2="1" y2="0">
          <stop offset="0" stop-color="#c86f7b"/>
          <stop offset="0.35" stop-color="#e4a6aa"/>
          <stop offset="0.55" stop-color="#5a2a33"/>
          <stop offset="0.75" stop-color="#e8c4c4"/>
          <stop offset="1" stop-color="#d8b6b6"/>
        </linearGradient>
      </defs>
      <polygon points="332,284 668,0 881,0 881,538 531,538" fill="url(#facetTone)"/>
    </svg>
    <div class="card-back__name">Marnie Veltrin</div>
  </section>
</div>
</body>
</html>
```